Harrowgate Supply Group Business Card Design

The Business Card will be one side only with Harrowgate Supplies Group Logo
Card should have:
Name
Title
Office phone Number
Cell Number
email address
Website
Street Address
Our Slogan is Rugged and Reliable
Looking for something that stands out from other business cards

Target Market(s)

Heavy equipment Lease Company

```html
<!DOCTYPE html>
<html lang="en">
<head>
<meta charset="utf-8">
<title>Harrowgate Supplies Group – Business Card</title>
<link rel="stylesheet" href="https://fonts.googleapis.com/css2?family=Open+Sans:wght@400;600;700&display=swap">
<style>
  :root {
    --navy: #2b2f8f;
    --red: #e8233f;
    --ink: #1c1c22;
    --paper: #ffffff;
    --backdrop: #e9e7e3;
  }
  * { margin: 0; padding: 0; box-sizing: border-box; }
  html, body { width: 1200px; height: 1023px; overflow: hidden; background: var(--backdrop); }
  body { font-family: "Open Sans", Arial, sans-serif; position: relative; }

  .business-card {
    position: absolute; left: 100px; top: 226px;
    width: 1000px; height: 571px;
    background: var(--paper);
    overflow: hidden;
    box-shadow: 0 6px 24px rgba(0,0,0,.12);
  }
  .card-graphics { position: absolute; inset: 0; }

  .brand {
    position: absolute; left: 150px; top: 70px;
    display: flex; align-items: center; gap: 14px;
  }
  .brand-mark { width: 30px; height: 30px; background: var(--navy); }
  .brand-name {
    font-weight: 700; font-size: 40px; color: var(--red);
    text-transform: uppercase; letter-spacing: .5px; line-height: 1;
  }
  .brand-rule {
    position: absolute; left: 150px; top: 132px;
    width: 640px; height: 2px; background: var(--navy);
  }
  .slogan {
    position: absolute; left: 470px; top: 150px;
    font-size: 30px; color: var(--red); font-weight: 400;
  }

  .person { position: absolute; left: 330px; top: 250px; }
  .person-name { font-size: 34px; font-weight: 600; color: var(--navy); line-height: 1.1; }
  .person-title { font-size: 22px; color: var(--red); }

  .contact-list {
    position: absolute; left: 330px; top: 345px;
    list-style: none; font-size: 21px; color: var(--ink);
  }
  .contact-list li { display: flex; align-items: center; gap: 14px; height: 37px; white-space: nowrap; }
  .contact-icon { width: 20px; height: 20px; flex: none; }
</style>
</head>
<body>
  <article class="business-card">
    <svg class="card-graphics" width="1000" height="571" viewBox="0 0 1000 571" aria-hidden="true">
      <polygon class="corner-band" points="0,330 0,571 600,571 600,552 320,552" fill="#2b2f8f"/>
      <rect class="accent-block" x="35" y="230" width="70" height="40" fill="#e8233f" transform="rotate(35 70 250)"/>
      <rect class="accent-block" x="115" y="290" width="70" height="40" fill="#e8233f" transform="rotate(35 150 310)"/>
      <rect class="accent-block" x="200" y="350" width="70" height="40" fill="#e8233f" opacity=".9" transform="rotate(35 235 370)"/>
    </svg>

    <div class="brand">
      <span class="brand-mark"></span>
      <span class="brand-name">Harrowgate Supplies Group</span>
    </div>
    <div class="brand-rule"></div>
    <p class="slogan">Rugged and Reliable</p>

    <div class="person">
      <p class="person-name">Dane Whitlock</p>
      <p class="person-title">Manager</p>
    </div>

    <ul class="contact-list">
      <li>
        <svg class="contact-icon" viewBox="0 0 20 20"><rect width="20" height="20" fill="#2b2f8f"/><rect x="5" y="4" width="10" height="12" fill="none" stroke="#fff" stroke-width="1.6"/></svg>
        626.555.0142
      </li>
      <li>
        <svg class="contact-icon" viewBox="0 0 20 20"><rect width="20" height="20" fill="#2b2f8f"/><path d="M6 5c0 5 4 9 9 9l1-2-3-1.5-1.5 1.2c-1.5-.7-2.5-1.7-3.2-3.2L9.5 7 8 4z" fill="#fff"/></svg>
        949.555.0173
      </li>
      <li>
        <svg class="contact-icon" viewBox="0 0 20 20"><rect width="20" height="20" fill="#2b2f8f"/><rect x="4" y="6" width="12" height="8" fill="none" stroke="#fff" stroke-width="1.4"/><path d="M4 6l6 5 6-5" fill="none" stroke="#fff" stroke-width="1.4"/></svg>
        whitlock@harrowgatesupply.com
      </li>
      <li>
        <svg class="contact-icon" viewBox="0 0 20 20"><rect width="20" height="20" fill="#2b2f8f"/><circle cx="10" cy="10" r="5.5" fill="none" stroke="#fff" stroke-width="1.4"/><path d="M4.5 10h11M10 4.5c-2.5 3-2.5 8 0 11M10 4.5c2.5 3 2.5 8 0 11" fill="none" stroke="#fff" stroke-width="1"/></svg>
        www.HarrowgateSupply.com
      </li>
      <li>
        <svg class="contact-icon" viewBox="0 0 20 20"><rect width="20" height="20" fill="#2b2f8f"/><path d="M10 16s-4.5-5-4.5-8a4.5 4.5 0 0 1 9 0c0 3-4.5 8-4.5 8z" fill="#fff"/><circle cx="10" cy="8" r="1.6" fill="#2b2f8f"/></svg>
        Sample Location D.B.A. Northfield Yard Dunmore, OR 97211
      </li>
    </ul>
  </article>
</body>
</html>
```